Flyer Design Project

New pest control company starting in southern maryland with the name Pest Raiders. We are going off the same kind of concept as the Shadowchasers. Our slogan is.....killing bugs its what we do best. The telephone number for the business is 240 555 0187. About us....we are a new exciting brand coming to the southern Maryland area offering a safer and more effective solution to pest control. We strive to use the safest and most effective products while providing the best and most effective service. We are a local based company with over ten years experience. As a special to all new Maryland clients we are offering the following coupons. 1. New customers get $100 off initial service which includes a termite inspection with a one year contract. 2. With a one year contract get 50 % off mosquito treatments normally $100 now $50 lawn treatments are done every 30 days. 3. Sign up before May 30th and receive lawn treatments for ticks and fleas up to half an acre included at no additional charge with a signed 1 year contract

Industry/Entity Type

```html
<!DOCTYPE html>
<html lang="en">
<head>
<meta charset="utf-8">
<title>Pest Raiders Flyer</title>
<link rel="stylesheet" href="https://fonts.googleapis.com/css2?family=Roboto+Condensed:wght@400;700;900&family=Lato:wght@400&display=swap">
<style>
  :root {
    --blue: #1432e0;
    --red: #ec1c24;
    --red-dark: #a8070d;
    --ink: #2e2e2e;
    --panel: #5e5e5e;
    --panel-dark: #4a4a4a;
    --white: #ffffff;
    --page: #e6e6e6;
  }
  * { margin: 0; padding: 0; box-sizing: border-box; }
  html, body { width: 1200px; height: 1200px; overflow: hidden; background: var(--page); }
  .flyer {
    position: absolute; left: 170px; top: 78px;
    width: 1052px; height: 1344px;
    transform: scale(0.8); transform-origin: 0 0;
    background: var(--white); overflow: hidden;
    box-shadow: 0 6px 24px rgba(0,0,0,.25);
  }
  .hero-photo {
    position: absolute; left: 0; top: 0; width: 1052px; height: 720px;
    background: linear-gradient(160deg, #c9d3dc 0%, #eef2f5 35%, #9fb08e 58%, #e9edf1 85%, #f3f5f7 100%);
  }
  .waves { position: absolute; left: 0; top: 0; }
  .headline { position: absolute; left: 540px; top: 86px; width: 455px; text-align: right; font-family: "Roboto Condensed", sans-serif; }
  .headline-kill { color: var(--red); font-weight: 900; font-size: 76px; line-height: 76px; display: block; }
  .headline-what { color: var(--ink); font-weight: 400; font-size: 74px; line-height: 82px; display: block; }
  .headline-best { color: var(--blue); font-weight: 900; font-size: 206px; line-height: 172px; display: block; letter-spacing: -2px; }
  .brand-name {
    position: absolute; left: 580px; top: 640px; width: 380px;
    display: flex; align-items: center; justify-content: center; gap: 16px;
    font-family: "Roboto Condensed", sans-serif; font-weight: 700; font-size: 56px; line-height: 64px;
    color: var(--blue);
  }
  .brand-dot { width: 40px; height: 40px; border-radius: 50%; background: var(--blue); flex: none; }
  .offer-panel { position: absolute; left: 43px; top: 603px; width: 442px; height: 760px;
    background: linear-gradient(180deg, var(--panel-dark), var(--panel) 40%); border-radius: 60px 60px 0 0; }
  .offer-ribbon { position: absolute; left: 12px; top: 653px; width: 502px; height: 72px; background: var(--red);
    color: var(--white); font-family: "Roboto Condensed", sans-serif; font-weight: 700; font-size: 33px; line-height: 30px;
    text-align: center; padding-top: 6px; }
  .ribbon-fold { position: absolute; top: 725px; width: 28px; height: 26px; background: var(--red-dark); }
  .ribbon-fold.left { left: 12px; clip-path: polygon(0 0, 100% 0, 100% 100%); }
  .ribbon-fold.right { left: 486px; clip-path: polygon(0 0, 100% 0, 0 100%); }
  .offer-item { position: absolute; left: 68px; width: 383px; color: var(--white); font-family: Lato, sans-serif;
    font-size: 26px; line-height: 31px; letter-spacing: 0.2px; text-align: justify; text-align-last: center; }
  .offer-divider { position: absolute; left: 58px; width: 408px; border-top: 2px dashed #d8d8d8; }
  .about-title { position: absolute; left: 556px; top: 818px; color: var(--red); font-family: "Roboto Condensed", sans-serif;
    font-weight: 700; font-size: 38px; }
  .about-text { position: absolute; left: 556px; top: 876px; width: 417px; color: #222; font-family: Lato, sans-serif;
    font-size: 23px; line-height: 27.4px; text-align: justify; }
  .call-box { position: absolute; left: 601px; top: 1128px; width: 309px; height: 116px; border: 2px solid #555;
    border-radius: 58px; text-align: center; font-family: "Roboto Condensed", sans-serif; font-weight: 700; background: var(--white); }
  .call-label { color: var(--red); font-size: 36px; line-height: 40px; margin-top: 8px; }
  .call-number { color: var(--ink); font-size: 52px; line-height: 56px; }
</style>
</head>
<body>
<main class="flyer">
  <div class="hero-photo" role="img" aria-label="Photo of a pest control technician in protective gear fogging trees in front of apartment buildings"></div>

  <svg class="waves" width="1052" height="1344" viewBox="0 0 1052 1344" aria-hidden="true">
    <path d="M0 625 C80 500 180 400 300 388 C420 378 520 440 640 510 C780 580 940 600 1052 585 L1052 1344 L0 1344 Z" fill="var(--blue)"/>
    <path d="M0 640 C120 520 240 460 340 458 C460 456 560 520 660 560 C800 610 950 620 1052 575 L1052 1344 L0 1344 Z" fill="var(--red)"/>
    <path d="M0 662 C130 545 250 485 340 483 C460 480 560 545 660 585 C800 640 950 650 1052 612 L1052 1344 L0 1344 Z" fill="var(--white)"/>
    <path d="M0 1140 L0 1344 L1052 1344 L1052 1160 C950 1260 800 1300 650 1270 C500 1240 300 1160 160 1150 C90 1145 40 1150 0 1140 Z" fill="var(--red)"/>
    <path d="M0 1170 L0 1344 L1052 1344 L1052 1200 C960 1290 800 1320 650 1300 C500 1280 300 1200 160 1190 C90 1185 40 1190 0 1170 Z" fill="var(--white)"/>
    <path d="M0 1210 L0 1344 L1052 1344 L1052 1230 C960 1310 800 1340 640 1320 C490 1300 300 1230 160 1220 C90 1215 40 1220 0 1210 Z" fill="var(--blue)"/>
  </svg>

  <h1 class="headline">
    <span class="headline-kill">KILLING BUGS</span>
    <span class="headline-what">its what we do</span>
    <span class="headline-best">BEST</span>
  </h1>

  <div class="brand-name"><span class="brand-dot"></span><span>PEST RAIDERS</span></div>

  <div class="offer-panel"></div>
  <div class="offer-ribbon">SPECIAL OFFER TO ALL NEW<br>MARYLAND CLIENTS</div>
  <div class="ribbon-fold left"></div>
  <div class="ribbon-fold right"></div>

  <p class="offer-item" style="top:750px">New customers get $100 off initial service which includes a termite inspection with a one year contract.</p>
  <div class="offer-divider" style="top:914px"></div>
  <p class="offer-item" style="top:937px">With a one year contract get 50 % off mosquito treatments normally $100 now $50 lawn treatments are done every 30 days.</p>
  <div class="offer-divider" style="top:1099px"></div>
  <p class="offer-item" style="top:1124px">Sign up before May 30th and receive lawn treatments for ticks and fleas up to half an acre included at no additional charge with a signed 1 year contract</p>

  <h2 class="about-title">ABOUT US</h2>
  <p class="about-text">We are a new exciting brand coming to the southern Maryland area offering a safer and more effective solution to pest control. We strive to use the safest and most effective products while providing the best and most effective service. We are a local based company with over ten years experience.</p>

  <div class="call-box">
    <div class="call-label">CALL US NOW</div>
    <div class="call-number">240 555 0187</div>
  </div>
</main>
</body>
</html>
```